Need Business Cards for my Business

email address: rkpmarlowhollowworks@vendrimail.com
web address: rkpmarlowhollowworks.net
Slogan: We offer various QVN licenses
Rowland K. Pemberly
Please stick with colors of Company Logo
would like the card to be more of the color example of the logo.
If you need PDF copy of logo email me at the above account.
Creative control rests with you.

Industry/Entity Type

Business

Contact Information for Business Card

I am a minimalist, but would like something to pop and stand out amongst other cards, make it memorable.

Font styles to use
Serif
Decorative
Script

```html
<!DOCTYPE html>
<html lang="en">
<head>
<meta charset="utf-8">
<title>Marlow Hollow Aero Testing – Business Cards</title>
<link href="https://fonts.googleapis.com/css2?family=Questrial&display=swap" rel="stylesheet">
<style>
  :root{
    --bg:#e9e7e3;
    --card:#f6f6f7;
    --red:#e0232b;
    --blue:#1467a8;
    --blue-dark:#0f4f86;
    --ink:#151515;
    --band:#0c0c0c;
    --white:#ffffff;
  }
  *{margin:0;padding:0;box-sizing:border-box}
  html,body{width:1200px;height:962px;overflow:hidden;background:var(--bg)}
  body{font-family:"Questrial",sans-serif;position:relative}
  .card{position:absolute;left:220px;width:760px;height:434px;border-radius:14px;overflow:hidden;
        box-shadow:0 6px 18px rgba(0,0,0,.18);background:var(--card)}
  .card--front{top:30px}
  .card--back{top:498px}
  .card svg{display:block}
  .brand-name{font-family:"Questrial",sans-serif;fill:var(--blue-dark);font-size:44px;letter-spacing:3px}
  .brand-line{font-family:"Questrial",sans-serif;fill:var(--blue-dark);font-size:22px;letter-spacing:5px}
  .holder-name{font-family:"Questrial",sans-serif;fill:var(--white);font-size:26px}
  .slogan{font-family:"Questrial",sans-serif;fill:var(--ink);font-size:24px}
  .contact{font-family:"Questrial",sans-serif;fill:var(--white);font-size:20px}
</style>
</head>
<body>

<section class="card card--front" aria-label="Card front">
  <svg width="760" height="434" viewBox="0 0 760 434">
    <rect class="card-base" width="760" height="434" fill="var(--card)"/>
    <polygon class="shape-red" points="0,0 420,0 0,175" fill="var(--red)"/>
    <polygon class="shape-blue" points="0,175 70,150 530,434 0,434" fill="var(--blue)"/>
    <rect class="brand-mark" x="232" y="190" width="28" height="28" fill="var(--blue-dark)"/>
    <text class="brand-name" x="274" y="220">MARLOW HOLLOW</text>
    <text class="brand-line" x="276" y="256">AERO TESTING</text>
  </svg>
</section>

<section class="card card--back" aria-label="Card back">
  <svg width="760" height="434" viewBox="0 0 760 434">
    <rect class="card-base" width="760" height="434" fill="var(--card)"/>
    <polygon class="shape-red" points="0,0 250,0 0,110" fill="var(--red)"/>
    <polygon class="shape-blue" points="0,110 40,95 330,434 0,434" fill="var(--blue)"/>

    <g class="details" transform="translate(250,40) rotate(18)">
      <rect class="name-band" x="0" y="0" width="470" height="46" fill="var(--band)"/>
      <polygon class="name-band-tip name-band-tip--blue" points="470,0 500,0 482,46 452,46" fill="var(--blue)"/>
      <polygon class="name-band-tip name-band-tip--red" points="500,0 530,0 512,46 482,46" fill="var(--red)"/>
      <text class="holder-name" x="120" y="32">Rowland K. Pemberly</text>
      <text class="slogan" x="40" y="84">We offer various QVN licenses</text>

      <rect class="icon-box icon-box--mail" x="-30" y="102" width="52" height="46" fill="var(--red)"/>
      <g class="icon-mail" fill="none" stroke="var(--white)" stroke-width="2">
        <rect x="-16" y="115" width="24" height="18"/>
        <polyline points="-16,115 -4,126 8,115"/>
      </g>
      <rect class="contact-band" x="22" y="102" width="640" height="46" fill="var(--band)"/>
      <text class="contact" x="44" y="132">rkpmarlowhollowworks@vendrimail.com</text>

      <rect class="icon-box icon-box--web" x="-30" y="158" width="52" height="46" fill="var(--blue)"/>
      <g class="icon-globe" fill="none" stroke="var(--white)" stroke-width="2">
        <circle cx="-4" cy="181" r="11"/>
        <ellipse cx="-4" cy="181" rx="5" ry="11"/>
        <line x1="-15" y1="181" x2="7" y2="181"/>
      </g>
      <rect class="contact-band" x="22" y="158" width="640" height="46" fill="var(--band)"/>
      <text class="contact" x="44" y="188">rkpmarlowhollowworks.net</text>
    </g>
  </svg>
</section>

</body>
</html>
```